Global Expert Network Firm needs business card design

We need business card design for a new company based in Seoul, South Korea called 'Corwell Insight Partners'. We recruit industry experts covering all countries and connect our client and recruited expert by phone, face-to-face meetings and etc. We are a global expert network firm that is focused on delivering high-quality experts to our clients throughout the world. Our clients include multinational corporations, global consulting firms, private equity firms, venture capital firms, asset management companies.
We have made new logo and please find attachment.(Please use new logo)
Target Market(s)
Global Consulting Firms, Investment Firms, Private Equity Firms, Venture Capital Firms.
Industry/Entity Type
Recruitment
Contact Information for Business Card
We need two Languages (English and Korean Version).
The front is Korean and the back is English version.
[The back] [English]
Company Name: Corwell Insight Partners, Inc.
CEO Name: Daniel Park
Address: #507, Hanbit Bldg, 82 Maebongsan-ro, Dobong-gu, Seoul, 01327, Korea
Tel. +82 2 718 4052
Fax. +82 2 864 1097
Mobile. +82 10 7264 8815
Email: daniel@corwellip.com
Web: www.corwellip.com
[The front] [Korean] => Described in same order as English version.
회사명: 코웰인사이트파트너스(주)
대표이사: 박도현
주소: 서울시 도봉구 매봉산로 82 한빛빌딩 507호
Tel. 02 718 4052
Fax. 02 864 1097
Mobile. 010 7264 8815
Web: www.corwellip.com
Look and feel
Each slider illustrates characteristics of the customer's brand and the style your logo design should communicate.

```html
<!DOCTYPE html>
<html lang="en">
<head>
<meta charset="utf-8">
<title>Corwell Insight Partners – Business Card</title>
<link rel="stylesheet" href="https://fonts.googleapis.com/css2?family=Figtree:wght@400;700&family=Nanum+Myeongjo&display=swap">
<style>
  :root {
    --page-top: #c4c4c4;
    --page-bottom: #a9a9a9;
    --card-dark: #2b2b2b;
    --card-light: #eeeeee;
    --ink-light: #ffffff;
    --ink-dark-muted: #d6d6d6;
    --navy: #262a52;
    --ink-body: #2c2c3a;
    --rule-dark: #6b6b6b;
    --rule-light: #b9b9c4;
  }
  * { margin: 0; padding: 0; box-sizing: border-box; }
  html, body { width: 1200px; height: 1057px; overflow: hidden; }
  body {
    background: linear-gradient(180deg, var(--page-top), var(--page-bottom));
    display: flex;
    align-items: center;
    justify-content: center;
    gap: 34px;
    font-family: "Figtree", "Helvetica Neue", Arial, sans-serif;
  }
  .card {
    width: 560px;
    height: 308px;
    position: relative;
    display: flex;
    align-items: stretch;
  }
  .card--english { background: var(--card-dark); color: var(--ink-dark-muted); }
  .card--korean { background: var(--card-light); color: var(--ink-body); }

  .brand {
    width: 272px;
    padding-left: 74px;
    display: flex;
    align-items: center;
    gap: 12px;
  }
  .brand__mark {
    width: 12px;
    height: 12px;
    flex: none;
    align-self: center;
  }
  .brand__name {
    font-family: "Figtree", "Helvetica Neue", Arial, sans-serif;
    font-weight: 400;
    font-size: 24px;
    line-height: 30px;
  }
  .card--english .brand__mark { background: var(--ink-light); }
  .card--english .brand__name { color: var(--ink-light); }
  .card--korean .brand__mark { background: var(--navy); }
  .card--korean .brand__name { color: var(--navy); }

  .divider {
    width: 1px;
    margin: 60px 0 52px;
  }
  .card--english .divider { background: var(--rule-dark); }
  .card--korean .divider { background: var(--rule-light); }

  .details {
    padding: 58px 0 0 36px;
    display: flex;
    flex-direction: column;
  }
  .details__name {
    font-size: 19px;
    font-weight: 700;
    color: var(--ink-light);
    line-height: 22px;
  }
  .details__title { font-size: 12px; line-height: 16px; margin-bottom: 14px; }
  .details__address { font-size: 12.5px; line-height: 18px; margin-bottom: 14px; }

  .card--korean .details { padding-top: 52px; }
  .card--korean .details__name {
    font-family: "Nanum Myeongjo", serif;
    font-weight: 400;
    font-size: 23px;
    line-height: 26px;
    color: var(--ink-body);
  }
  .card--korean .details__title,
  .card--korean .details__address {
    font-family: "Nanum Myeongjo", serif;
    font-size: 14px;
  }
  .card--korean .details__address { line-height: 19px; }

  .contact { list-style: none; font-size: 12.5px; line-height: 18px; }
  .contact li { display: flex; align-items: center; gap: 10px; }
  .contact svg { width: 11px; height: 11px; flex: none; }
  .card--english .contact svg { color: var(--ink-dark-muted); }
  .card--korean .contact svg { color: var(--ink-body); }
  .icon-set { position: absolute; width: 0; height: 0; }
</style>
</head>
<body>

<svg class="icon-set" aria-hidden="true">
  <defs>
    <symbol id="icon-phone" viewBox="0 0 16 16">
      <path d="M4 1.5l2.3 2.8-1.4 1.8c.9 2 2.6 3.8 4.7 4.8l1.8-1.4 2.8 2.3-1.3 2.2C7.5 13.7 2.3 8.5 1.8 3z" fill="currentColor"/>
    </symbol>
    <symbol id="icon-fax" viewBox="0 0 16 16">
      <rect x="4" y="1.5" width="8" height="4" fill="none" stroke="currentColor" stroke-width="1.4"/>
      <rect x="1" y="5.5" width="14" height="6.5" rx="1" fill="currentColor"/>
      <rect x="4" y="10" width="8" height="4.5" fill="currentColor" stroke="#fff" stroke-width=".8"/>
    </symbol>
    <symbol id="icon-mobile" viewBox="0 0 16 16">
      <rect x="4" y="1" width="8" height="14" rx="1.2" fill="none" stroke="currentColor" stroke-width="1.4"/>
      <circle cx="8" cy="12.5" r=".9" fill="currentColor"/>
    </symbol>
    <symbol id="icon-mail" viewBox="0 0 16 16">
      <rect x="1" y="3" width="14" height="10" fill="none" stroke="currentColor" stroke-width="1.2"/>
      <path d="M1 3l7 6 7-6M1 13l5-5M15 13l-5-5" fill="none" stroke="currentColor" stroke-width="1.2"/>
    </symbol>
    <symbol id="icon-web" viewBox="0 0 16 16">
      <g fill="none" stroke="currentColor" stroke-width="1.1">
        <circle cx="8" cy="8" r="6.8"/>
        <ellipse cx="8" cy="8" rx="3" ry="6.8"/>
        <path d="M1.2 8h13.6M2.3 4.5h11.4M2.3 11.5h11.4"/>
      </g>
    </symbol>
  </defs>
</svg>

<section class="card card--english" aria-label="Business card, English side">
  <div class="brand">
    <span class="brand__mark" aria-hidden="true"></span>
    <p class="brand__name">Corwell<br>Insight<br>Partners</p>
  </div>
  <div class="divider"></div>
  <div class="details">
    <h1 class="details__name">Daniel PARK</h1>
    <p class="details__title">CEO</p>
    <p class="details__address">#507, Hanbit Bldg<br>82 Maebongsan-ro<br>Dobong-gu, Seoul, 01327, Korea</p>
    <ul class="contact">
      <li><svg><use href="#icon-phone"/></svg>+82 2 718 4052</li>
      <li><svg><use href="#icon-fax"/></svg>+82 2 864 1097</li>
      <li><svg><use href="#icon-mobile"/></svg>+82 10 7264 8815</li>
      <li><svg><use href="#icon-mail"/></svg>daniel@corwellip.com</li>
      <li><svg><use href="#icon-web"/></svg>www.corwellip.com</li>
    </ul>
  </div>
</section>

<section class="card card--korean" aria-label="Business card, Korean side" lang="ko">
  <div class="brand">
    <span class="brand__mark" aria-hidden="true"></span>
    <p class="brand__name" lang="en">Corwell<br>Insight<br>Partners</p>
  </div>
  <div class="divider"></div>
  <div class="details">
    <h2 class="details__name">박도현</h2>
    <p class="details__title">대표이사</p>
    <p class="details__address">서울시 도봉구 매봉산로<br>82 한빛빌딩 507호</p>
    <ul class="contact">
      <li><svg><use href="#icon-phone"/></svg>+82 2 718 4052</li>
      <li><svg><use href="#icon-fax"/></svg>+82 2 864 1097</li>
      <li><svg><use href="#icon-mobile"/></svg>+82 10 7264 8815</li>
      <li><svg><use href="#icon-mail"/></svg>daniel@corwellip.com</li>
      <li><svg><use href="#icon-web"/></svg>www.corwellip.com</li>
    </ul>
  </div>
</section>

</body>
</html>
```